Business Card Ayurvedic Massage

I'm starting with my ayurvedic massage business and need a business card design. The design should be inline with my brand/logo as well as with the design of my website (www.lumo-thara.ch).
Front: logo and text "Ayurvedische Massagen"
back: name and adress (see details https://www.lumo-thara.ch/kontakt.html)

```html
<!DOCTYPE html>
<html lang="de">
<head>
<meta charset="utf-8">
<title>Lumo-Thara – Ayurvedische Massagen</title>
<link rel="stylesheet" href="https://fonts.googleapis.com/css2?family=Open+Sans:wdth,wght@75..100,400..800&display=swap">
<style>
  :root {
    --bg-red: #6c0905;
    --bg-red-light: #7e0f08;
    --ink: #1b0705;
    --accent-orange: #f07a2a;
    --gold: #e3a436;
    --band-red: #e8160c;
    --band-orange: #f86a10;
    --band-yellow: #fbe80c;
    --bullet-core: #f9d50f;
    --bullet-edge: #e7760d;
  }
  html, body {
    margin: 0;
    padding: 0;
    width: 1200px;
    height: 720px;
    overflow: hidden;
    background: var(--bg-red);
  }
  .card {
    position: relative;
    width: 1200px;
    height: 720px;
    overflow: hidden;
    font-family: "Open Sans", Arial, sans-serif;
    font-stretch: 87.5%;
    background: radial-gradient(ellipse at 45% 45%, var(--bg-red-light) 0%, var(--bg-red) 70%);
  }
  .brand {
    position: absolute;
    left: 114px;
    top: 240px;
    width: 464px;
    height: 158px;
    display: flex;
    align-items: center;
    justify-content: center;
  }
  .brand-name {
    font-size: 44px;
    font-weight: 600;
    color: var(--gold);
    letter-spacing: 1px;
  }
  .divider {
    position: absolute;
    left: 614px;
    top: 160px;
    width: 1.5px;
    height: 340px;
    background: #1a0503;
  }
  .website {
    position: absolute;
    left: 644px;
    top: 163px;
    margin: 0;
    font-size: 23px;
    font-weight: 500;
    color: var(--accent-orange);
    letter-spacing: 0.5px;
  }
  .menu {
    position: absolute;
    left: 690px;
    top: 228px;
    margin: 0;
    padding: 0;
    list-style: none;
  }
  .menu-item {
    display: flex;
    align-items: center;
    height: 54px;
    font-size: 43px;
    font-weight: 600;
    color: var(--ink);
    letter-spacing: 1.5px;
  }
  .bullet {
    width: 38px;
    height: 38px;
    margin-right: 43px;
    flex: none;
  }
  .tagline-band {
    position: absolute;
    left: 0;
    top: 635px;
    width: 1200px;
    height: 46px;
    display: flex;
    align-items: center;
    justify-content: center;
    background: linear-gradient(to bottom,
      var(--band-red) 0%,
      var(--band-orange) 22%,
      var(--band-yellow) 50%,
      var(--band-orange) 78%,
      var(--band-red) 100%);
  }
  .tagline {
    margin: 0;
    font-size: 27px;
    font-weight: 700;
    color: var(--ink);
    letter-spacing: 1.5px;
  }
</style>
</head>
<body>
<main class="card">
  <div class="brand">
    <span class="brand-name">lumo-thara</span>
  </div>

  <div class="divider"></div>

  <p class="website">HTTP://WWW.LUMO-THARA.CH</p>

  <ul class="menu">
    <li class="menu-item"><svg class="bullet" viewBox="0 0 40 40" aria-hidden="true"><defs><radialGradient id="b1"><stop offset="0" stop-color="var(--bullet-core)"/><stop offset="1" stop-color="var(--bullet-edge)"/></radialGradient></defs><circle cx="20" cy="20" r="18" fill="url(#b1)"/></svg>AYURVEDA</li>
    <li class="menu-item"><svg class="bullet" viewBox="0 0 40 40" aria-hidden="true"><circle cx="20" cy="20" r="18" fill="url(#b1)"/></svg>BEHANDLUNGEN</li>
    <li class="menu-item"><svg class="bullet" viewBox="0 0 40 40" aria-hidden="true"><circle cx="20" cy="20" r="18" fill="url(#b1)"/></svg>PREISE</li>
    <li class="menu-item"><svg class="bullet" viewBox="0 0 40 40" aria-hidden="true"><circle cx="20" cy="20" r="18" fill="url(#b1)"/></svg>PRAXIS</li>
  </ul>

  <div class="tagline-band">
    <p class="tagline">AYURVEDISCHE MASSAGEN</p>
  </div>
</main>
</body>
</html>
```